Ironvale Holdings Business card

We need a an amazing matte black and gold card! W are a finance investing company so we want something that's eye catching and sleek. We want it to be attractive and sleek and represent money. Heck with would like the letters and lgo to be printed as 24k gold one day. We have the logo added so please use the color scheme with the logo and have that beautifully placed on one side.

Target Market(s)

Investors of all ages

Industry/Entity Type

Financial

Contact Information for Business Card

Black and matte with gold lettering follow logo colrs please.

Font styles to use
Other font styles liked:
• you decide

Colors

Designer to choose colors to be used in the design.

Requirements
Must have
• Matte Black and Gold, logo on one side. job title and name , website, phone number and email address on the other side
Nice to have
• Matte black and crisp finish to attract investors
Should not have
• playful, very professional!

```html
<!DOCTYPE html>
<html lang="en">
<head>
<meta charset="UTF-8">
<title>Ironvale Holdings Business Card</title>
<link rel="stylesheet" href="https://fonts.googleapis.com/css2?family=Arimo:wght@400;700&display=swap">
<style>
  :root {
    --backdrop: #1a1a1a;
    --card-black: #060606;
    --gold: #d9b43a;
    --gold-line: #c9a230;
    --white: #f2f2f2;
  }
  html, body {
    margin: 0;
    padding: 0;
    width: 1200px;
    height: 1200px;
    overflow: hidden;
    background: var(--backdrop);
    font-family: "Arimo", Arial, sans-serif;
  }
  .stage {
    position: relative;
    width: 1200px;
    height: 1200px;
  }
  .card {
    position: absolute;
    left: 192px;
    width: 816px;
    height: 523px;
    background: var(--card-black);
    box-shadow: 0 10px 30px rgba(0,0,0,0.6);
  }
  .card--front { top: 72px; }
  .card--back { top: 643px; }
  .gold-rule {
    position: absolute;
    left: 0;
    right: 0;
    height: 6px;
    background: var(--gold-line);
  }
  .card--front .gold-rule { top: 480px; }
  .card--back .gold-rule { top: 485px; }
  .brand-name {
    position: absolute;
    left: 0;
    right: 0;
    text-align: center;
    color: var(--gold);
    font-weight: 700;
    margin: 0;
    line-height: 1;
  }
  .brand-name .brand-main {
    display: block;
    font-size: 58px;
    letter-spacing: 2px;
  }
  .brand-name .brand-sub {
    display: block;
    font-size: 30px;
    letter-spacing: 8px;
    margin-top: 16px;
  }
  .card--front .brand-name { top: 182px; }
  .card--back .brand-name { top: 108px; }
  .holder {
    position: absolute;
    right: 432px;
    top: 240px;
    text-align: right;
  }
  .holder-name {
    margin: 0;
    color: var(--gold);
    font-weight: 700;
    font-size: 36px;
    line-height: 1.1;
  }
  .holder-title {
    margin: 4px 0 0;
    color: var(--white);
    font-size: 19px;
  }
  .divider {
    position: absolute;
    left: 406px;
    top: 226px;
    width: 2px;
    height: 88px;
    background: var(--gold-line);
  }
  .contact-list {
    position: absolute;
    left: 446px;
    top: 226px;
    margin: 0;
    padding: 0;
    list-style: none;
  }
  .contact-item {
    display: flex;
    align-items: center;
    height: 29px;
    color: var(--white);
    font-size: 17px;
  }
  .contact-item svg {
    width: 18px;
    height: 18px;
    margin-right: 23px;
    flex: none;
  }
</style>
</head>
<body>
<div class="stage">
  <section class="card card--front">
    <h1 class="brand-name">
      <span class="brand-main">IRONVALE</span>
      <span class="brand-sub">HOLDINGS</span>
    </h1>
    <div class="gold-rule"></div>
  </section>

  <section class="card card--back">
    <h2 class="brand-name">
      <span class="brand-main">IRONVALE</span>
      <span class="brand-sub">HOLDINGS</span>
    </h2>
    <div class="holder">
      <p class="holder-name">Daniel Hart</p>
      <p class="holder-title">Managing Director</p>
    </div>
    <div class="divider"></div>
    <ul class="contact-list">
      <li class="contact-item">
        <svg viewBox="0 0 24 24" aria-hidden="true"><path fill="#d9b43a" d="M6.6 10.8a15.1 15.1 0 0 0 6.6 6.6l2.2-2.2a1 1 0 0 1 1-.25 11.4 11.4 0 0 0 3.6.57 1 1 0 0 1 1 1V20a1 1 0 0 1-1 1A17 17 0 0 1 3 4a1 1 0 0 1 1-1h3.5a1 1 0 0 1 1 1c0 1.25.2 2.45.57 3.57a1 1 0 0 1-.25 1z"/></svg>
        00 000 000 000
      </li>
      <li class="contact-item">
        <svg viewBox="0 0 24 24" aria-hidden="true"><rect x="2.5" y="5" width="19" height="14" fill="none" stroke="#d9b43a" stroke-width="2"/><path d="M2.5 5l9.5 8 9.5-8" fill="none" stroke="#d9b43a" stroke-width="2"/></svg>
        info@ironvaleholdings.com
      </li>
      <li class="contact-item">
        <svg viewBox="0 0 24 24" aria-hidden="true"><g fill="none" stroke="#d9b43a" stroke-width="1.8"><circle cx="12" cy="12" r="9.5"/><ellipse cx="12" cy="12" rx="4.2" ry="9.5"/><path d="M2.5 12h19M4 7h16M4 17h16"/></g></svg>
        www.ironvaleholdings.com
      </li>
    </ul>
    <div class="gold-rule"></div>
  </section>
</div>
</body>
</html>
```